" A empresa em questao será uma clínica médica e de fisioterapia especializada em tratamento de coluna. Tanto os médicos quanto os tratamentos fisioterápicos (fisioterapia, osteopatia, RPG) serao direcionados para o público que busca tratamento e soluçoes para dores nas costas em geral. "

```html
<!DOCTYPE html>
<html lang="pt-BR">
<head>
<meta charset="utf-8">
<title>Instituto Eixo Vital — Pasta</title>
<link rel="stylesheet" href="https://fonts.googleapis.com/css2?family=Montserrat:wght@400&display=swap">
<style>
  :root {
    --backdrop: #e9e6e1;
    --paper: #ffffff;
    --ink: #0b0b0b;
    --brand-white: #f4f4f4;
    --silver-light: #f2f2f2;
    --silver-dark: #a9a9a9;
    --fine-print: #8a8a8a;
  }
  * { margin: 0; padding: 0; box-sizing: border-box; }
  html, body {
    width: 1200px;
    height: 1200px;
    overflow: hidden;
    background: var(--backdrop);
  }
  .canvas {
    position: relative;
    width: 1200px;
    height: 1200px;
  }
  .folder {
    position: absolute;
    left: 130px;
    top: 186px;
    width: 941px;
    height: 828px;
  }
  .folder-shapes {
    position: absolute;
    inset: 0;
    width: 941px;
    height: 828px;
  }
  .brand {
    position: absolute;
    display: flex;
    align-items: center;
    font-family: "Montserrat", sans-serif;
    font-weight: 400;
    color: var(--brand-white);
    text-transform: uppercase;
    line-height: 1.2;
  }
  .brand-dot {
    border: 2px solid var(--brand-white);
    border-radius: 50%;
    flex: none;
  }
  .brand-cover {
    left: 662px;
    top: 500px;
    gap: 18px;
    font-size: 22px;
    letter-spacing: 1px;
  }
  .brand-cover .brand-dot { width: 40px; height: 40px; }
  .brand-pocket {
    left: 40px;
    top: 700px;
    gap: 9px;
    font-size: 12px;
    letter-spacing: 0.6px;
    transform: rotate(180deg);
  }
  .brand-pocket .brand-dot { width: 22px; height: 22px; border-width: 1.5px; }
  .address {
    position: absolute;
    left: 36px;
    top: 624px;
    font-family: "Montserrat", sans-serif;
    font-size: 8px;
    color: var(--fine-print);
    line-height: 1.5;
  }
</style>
</head>
<body>
<main class="canvas">
  <section class="folder">
    <svg class="folder-shapes" viewBox="0 0 392 345" preserveAspectRatio="none">
      <defs>
        <linearGradient id="emblem-fill" x1="0" y1="0" x2="1" y2="1">
          <stop offset="0" stop-color="var(--silver-light)"/>
          <stop offset="1" stop-color="var(--silver-dark)"/>
        </linearGradient>
      </defs>
      <rect class="page-inside" x="0" y="0" width="197" height="345" fill="var(--paper)"/>
      <rect class="page-cover" x="197" y="0" width="195" height="270" fill="var(--ink)"/>
      <circle class="emblem-area" cx="178" cy="120" r="118" fill="url(#emblem-fill)" opacity="0.55" role="img" aria-label="Emblema decorativo da coluna vertebral da clínica"/>
      <path class="pocket" d="M0,266 C90,268 165,258 197,222 L197,345 L0,345 Z" fill="var(--ink)"/>
    </svg>

    <p class="address">Rua das Palmeiras, 120 Bairro Jardim Sul<br>Cidade Nova · Cep 00.000-000</p>

    <div class="brand brand-cover">
      <span class="brand-dot"></span>
      <span class="brand-name">Instituto<br>Eixo Vital</span>
    </div>

    <div class="brand brand-pocket">
      <span class="brand-dot"></span>
      <span class="brand-name">Instituto<br>Eixo Vital</span>
    </div>
  </section>
</main>
</body>
</html>
```